Tovrelan Ltda

Logo design focused on: - Construction of civil works - Electrical services - Metal structures - Equipment rental Tomás Ibarra Leiva Manager tovrelan.ltda@brevomail.example 56 9 48215037 Quelitoco s / n, Sorimar, San Pedro de Atacama

Building

Colors
33a6d7
0292cd
33b8a4
0555a3

```html
<!DOCTYPE html>
<html lang="en">
<head>
<meta charset="utf-8">
<title>Tovrelan Ltda – Business Card</title>
<link rel="stylesheet" href="https://fonts.googleapis.com/css2?family=Montserrat:wght@500;600;700&display=swap">
<style>
  :root {
    --stage: #111111;
    --card: #ffffff;
    --soft-grey: #ececee;
    --teal-light: #33b8c4;
    --teal: #1eaab8;
    --sky: #33a6d7;
    --azure: #0292cd;
    --navy: #0555a3;
    --ink: #1d3f74;
    --white: #ffffff;
  }
  * { margin: 0; padding: 0; box-sizing: border-box; }
  html, body {
    width: 1200px; height: 1000px; overflow: hidden;
    background: var(--stage);
    font-family: "Montserrat", sans-serif;
  }
  .business-card {
    position: absolute; left: 100px; top: 215px;
    width: 1000px; height: 571px;
    background: var(--card);
    border-radius: 22px;
    overflow: hidden;
  }
  .grey-field {
    position: absolute; right: 0; top: 80px;
    width: 330px; height: 410px;
    background: var(--soft-grey);
    border-top-left-radius: 180px;
  }
  .brand {
    position: absolute; left: 70px; top: 70px;
    display: flex; align-items: center; gap: 22px;
  }
  .brand-dot {
    width: 82px; height: 82px; border-radius: 50%;
    background: var(--azure);
  }
  .brand-name {
    font-weight: 700; font-size: 52px; letter-spacing: 1px;
    color: var(--navy); text-transform: uppercase;
  }
  .address {
    position: absolute; right: 70px; top: 150px;
    font-weight: 500; font-size: 20px; line-height: 1.3;
    color: var(--ink); text-align: left;
  }
  .info-band {
    position: absolute; left: 0; top: 232px;
    width: 100%; height: 250px;
    background: linear-gradient(100deg, var(--teal-light) 0%, var(--teal) 55%, var(--sky) 100%);
  }
  .band-notch {
    position: absolute; left: 120px; top: 218px;
    width: 0; height: 0;
    border-left: 15px solid transparent; border-right: 15px solid transparent;
    border-bottom: 15px solid var(--teal-light);
  }
  .contact {
    position: absolute; left: 70px; top: 262px; color: var(--ink);
  }
  .contact-name {
    font-weight: 700; font-size: 30px; color: var(--white);
    text-transform: uppercase; letter-spacing: 0.5px;
  }
  .contact-role { font-weight: 600; font-size: 20px; margin-top: 2px; }
  .contact-line {
    display: flex; align-items: center; gap: 14px;
    font-weight: 600; font-size: 21px; margin-top: 14px;
  }
  .contact-line svg { width: 20px; height: 20px; fill: var(--white); }
  .services {
    position: absolute; left: 560px; top: 290px;
    list-style: none; color: var(--ink);
    font-weight: 700; font-size: 23px; line-height: 1.45;
  }
  .services li::before {
    content: ""; display: inline-block;
    width: 9px; height: 9px; border-radius: 50%;
    background: var(--white); margin: 0 14px 4px 0;
  }
  .bottom-rule-thin {
    position: absolute; left: 0; top: 490px;
    width: 100%; height: 3px; background: var(--azure);
  }
  .bottom-rule {
    position: absolute; left: 0; top: 500px;
    width: 100%; height: 10px; background: var(--navy);
  }
</style>
</head>
<body>
  <div class="business-card">
    <div class="grey-field" role="img" aria-label="Soft grey background field"></div>

    <div class="brand">
      <div class="brand-dot"></div>
      <div class="brand-name">Tovrelan Ltda</div>
    </div>

    <p class="address">Quelitoco s / n, Sorimar<br>San Pedro de Atacama</p>

    <div class="band-notch"></div>
    <div class="info-band"></div>

    <div class="contact">
      <div class="contact-name">Tomás Ibarra Leiva</div>
      <div class="contact-role">Manager</div>
      <div class="contact-line">
        <svg viewBox="0 0 24 24" aria-hidden="true"><path d="M6.6 10.8a15 15 0 0 0 6.6 6.6l2.2-2.2c.3-.3.7-.4 1-.2 1.1.4 2.3.6 3.6.6.6 0 1 .4 1 1V20c0 .6-.4 1-1 1A17 17 0 0 1 3 4c0-.6.4-1 1-1h3.5c.6 0 1 .4 1 1 0 1.3.2 2.5.6 3.6.1.3 0 .7-.2 1z"/></svg>
        <span>56 9 48215037</span>
      </div>
      <div class="contact-line">
        <svg viewBox="0 0 24 24" aria-hidden="true"><path d="M2 5h20v14H2z M3 6l9 7 9-7" fill="#ffffff" stroke="#1eaab8" stroke-width="1.5"/></svg>
        <span>tovrelan.ltda@brevomail.example</span>
      </div>
    </div>

    <ul class="services">
      <li>Construction of civil works</li>
      <li>Electrical services</li>
      <li>Metal structures</li>
      <li>Equipment rental</li>
    </ul>

    <div class="bottom-rule-thin"></div>
    <div class="bottom-rule"></div>
  </div>
</body>
</html>
```